Fahrzeugbeschriftung für Gipser/Maler, Fassadenbauer und Kundenmaurer
Zielgruppe
Wir sind Gipser/Maler, Fassadenbauer und Kundenmaurer
Aufgabenstellung
Wir möchten ein minimalistisches Design aber mit einem Akzent der Auffällig ist.

```html
<!DOCTYPE html>
<html lang="de">
<head>
<meta charset="utf-8">
<title>Fahrzeugbeschriftung – Putzwerk Helmreich</title>
<link rel="stylesheet" href="https://fonts.googleapis.com/css2?family=Roboto:wght@400;700;900&family=Poppins:wght@400&display=swap">
<style>
  :root {
    --yellow: #f2d32a;
    --dark: #2e2e2e;
    --white: #ffffff;
    --panel-edge: #d9d9d9;
    --bg-top: #959595;
    --bg-bottom: #c6c6c6;
  }
  html, body {
    margin: 0;
    padding: 0;
    overflow: hidden;
  }
  .canvas {
    position: relative;
    width: 980px;
    height: 1200px;
    overflow: hidden;
    background: linear-gradient(180deg, var(--bg-top) 0%, var(--bg-bottom) 100%);
  }
  .wrap-side {
    position: absolute;
    left: 34px;
    top: 70px;
    width: 903px;
    height: 347px;
  }
  .wrap-rear {
    position: absolute;
    left: 243px;
    top: 542px;
    width: 497px;
    height: 457px;
  }
  .body-panel { fill: var(--white); stroke: var(--panel-edge); stroke-width: 2; }
  .accent-yellow { fill: var(--yellow); }
  .accent-dark { fill: var(--dark); }
  .divider { stroke: var(--dark); stroke-width: 1.5; opacity: .5; }
  .rule-light { stroke: #cfcfcf; stroke-width: 2; }

  .kicker { font-family: 'Roboto', sans-serif; font-weight: 700; fill: var(--dark); }
  .headline { font-family: 'Roboto', sans-serif; font-weight: 900; fill: var(--dark); }
  .subline { font-family: 'Roboto', sans-serif; font-weight: 700; fill: var(--dark); }
  .service { font-family: 'Roboto', sans-serif; font-weight: 700; fill: var(--dark); }
  .brand-name { font-family: 'Poppins', sans-serif; font-weight: 400; fill: var(--white); }
  .phone { font-family: 'Roboto', sans-serif; font-weight: 700; fill: var(--dark); }
  .web { font-family: 'Roboto', sans-serif; font-weight: 400; fill: var(--dark); }
  .licensed { font-family: 'Roboto', sans-serif; font-weight: 700; fill: var(--dark); }
  .on-dark { fill: var(--white); }
</style>
</head>
<body>
<div class="canvas">

  <svg width="0" height="0" style="position:absolute">
    <defs>
      <symbol id="icon-tick" viewBox="0 0 20 20">
        <circle cx="10" cy="10" r="10" fill="#2e2e2e"/>
        <polyline points="5.5,10.5 8.8,13.5 14.5,7" fill="none" stroke="#fff" stroke-width="2.6" stroke-linecap="round" stroke-linejoin="round"/>
      </symbol>
      <symbol id="icon-phone" viewBox="0 0 20 20">
        <path d="M5 1.5 L8 5.5 L6.3 7.6 C7.3 9.8 9.6 12.3 12.4 13.7 L14.5 12 L18.5 15 L16.8 18.3 C9 18 2 11 1.7 3.2 Z" fill="currentColor"/>
      </symbol>
      <symbol id="icon-globe" viewBox="0 0 20 20">
        <circle cx="10" cy="10" r="9" fill="currentColor"/>
        <circle cx="10" cy="10" r="5" fill="none" stroke="#fff" stroke-width="1.3"/>
        <line x1="5" y1="10" x2="15" y2="10" stroke="#fff" stroke-width="1.3"/>
      </symbol>
    </defs>
  </svg>

  <!-- Side panel -->
  <svg class="wrap-side" viewBox="60 125 1600 615" aria-label="Seitenansicht der Fahrzeugbeschriftung">
    <rect class="body-panel" x="61" y="126" width="1598" height="613" rx="40"/>
    <polygon class="accent-yellow" points="1210,126 1630,126 1659,180 1659,370 1265,739 570,739"/>
    <polygon class="accent-yellow" points="625,660 1245,660 1185,739 570,739"/>

    <rect class="accent-dark" x="922" y="400" width="353" height="203"/>
    <text class="brand-name" x="955" y="475" font-size="52">Putzwerk</text>
    <text class="brand-name" x="955" y="535" font-size="52">Helmreich</text>

    <rect class="accent-dark" x="61" y="603" width="1598" height="57"/>
    <polygon class="accent-yellow" points="625,660 1245,660 1185,739 570,739"/>
    <line class="divider" x1="695" y1="126" x2="695" y2="739"/>
    <line class="divider" x1="1096" y1="126" x2="1098" y2="400"/>
    <line class="divider" x1="1098" y1="660" x2="1098" y2="739"/>

    <text class="kicker" x="757" y="275" font-size="15">PROFESSIONELL</text>
    <text class="headline" x="757" y="311" font-size="37">VERPUTZEN &amp;</text>
    <text class="subline" x="757" y="337" font-size="23">MALERARBEITEN</text>

    <use href="#icon-tick" x="1313" y="270" width="19" height="19"/>
    <text class="service" x="1345" y="289" font-size="27">PLASTERING</text>
    <use href="#icon-tick" x="1313" y="305" width="19" height="19"/>
    <text class="service" x="1345" y="324" font-size="27">FACADES</text>
    <use href="#icon-tick" x="1313" y="340" width="19" height="19"/>
    <text class="service" x="1345" y="359" font-size="27">PAINTING</text>
    <use href="#icon-tick" x="1313" y="376" width="19" height="19"/>
    <text class="service" x="1345" y="395" font-size="27">BRICKWORK</text>

    <use href="#icon-phone" x="404" y="527" width="21" height="21" style="color:#2e2e2e"/>
    <text class="phone" x="428" y="549" font-size="31">012-345-6789</text>
    <use href="#icon-globe" x="406" y="559" width="14" height="14" style="color:#2e2e2e"/>
    <text class="web" x="428" y="572" font-size="21">www.yourwebsite.com</text>

    <text class="licensed" x="954" y="706" font-size="29" text-anchor="middle">FULLY LICENSED &amp; INSURED</text>
  </svg>

  <!-- Rear panel -->
  <svg class="wrap-rear" viewBox="430 960 880 810" aria-label="Heckansicht der Fahrzeugbeschriftung">
    <rect class="body-panel" x="431" y="961" width="878" height="808" rx="50"/>
    <polygon class="accent-yellow" points="480,961 830,961 431,1345 431,1030"/>
    <polygon class="accent-dark" points="1309,1310 1309,1720 1259,1769 822,1769"/>
    <line class="divider" x1="868" y1="961" x2="868" y2="1769"/>

    <rect class="accent-dark" x="520" y="1310" width="276" height="221"/>
    <text class="brand-name" x="546" y="1417" font-size="40">Putzwerk</text>
    <text class="brand-name" x="546" y="1461" font-size="40">Helmreich</text>

    <text class="kicker" x="908" y="1089" font-size="18">PROFESSIONELL</text>
    <text class="headline" x="908" y="1131" font-size="43">VERPUTZEN &amp;</text>
    <text class="subline" x="908" y="1161" font-size="28">MALERARBEITEN</text>

    <use href="#icon-tick" x="908" y="1210" width="16" height="16"/>
    <text class="service" x="935" y="1226" font-size="23">PLASTERING</text>
    <use href="#icon-tick" x="908" y="1241" width="16" height="16"/>
    <text class="service" x="935" y="1257" font-size="23">FACADES</text>
    <use href="#icon-tick" x="908" y="1272" width="16" height="16"/>
    <text class="service" x="935" y="1288" font-size="23">PAINTING</text>
    <use href="#icon-tick" x="908" y="1303" width="16" height="16"/>
    <text class="service" x="935" y="1319" font-size="23">BRICKWORK</text>

    <text class="licensed on-dark" x="1226" y="1549" font-size="28" text-anchor="end">FULLY</text>
    <text class="licensed on-dark" x="1226" y="1579" font-size="28" text-anchor="end">LICENSED &amp;</text>
    <text class="licensed on-dark" x="1226" y="1609" font-size="28" text-anchor="end">INSURED</text>
    <line class="rule-light" x1="995" y1="1636" x2="1226" y2="1636"/>

    <use href="#icon-phone" x="957" y="1667" width="23" height="23" style="color:#f2d32a"/>
    <text class="phone on-dark" x="985" y="1695" font-size="39">012-345-6789</text>
    <use href="#icon-globe" x="960" y="1706" width="16" height="16" style="color:#f2d32a"/>
    <text class="web on-dark" x="985" y="1721" font-size="24">www.yourwebsite.com</text>
  </svg>

</div>
</body>
</html>
```